Cardiology Practice needs a Heart Scan Order Form

Busy cardiology practice needs an order form for a heart scan test. Sample is attached. One side should have all information noted and the other side should have our physician names (Dorian Velko, MD, L.N. Morvesti, MD, Ovila Brandt, MD, Tomas Velko, MD, and Gerald Pompetti, MD. It should have the map that is uploaded and our demographic information (Crestfield Cardiac PLLC, 712 Harrow Ln. Ste. K, Melrick, TX 77431 along with phone 832-417-2286 and fax 832-417-2287) as well as our web address (crestfieldcardiac.example). Our primary colors are red, black and white. Needs to fit paper size 8 1/2 by 11.

Target Market(s)

Healthcare

Industry/Entity Type

Health Care

Font styles to use
Serif

Colors
ec1f27

Requirements
Must have
• Logo, information listed on sample form, demographics and physician names as well as website.
Nice to have
• Open to suggestions
Should not have
• Physician Pictures

```html
<!DOCTYPE html>
<html lang="en">
<head>
<meta charset="utf-8">
<title>Crestfield Cardiac – Calcium Score Heart Scan Order Form</title>
<link href="https://fonts.googleapis.com/css2?family=Montserrat:wght@300;400;500;600;700;800;900&family=Roboto:ital,wght@0,400;0,500;0,700;1,500;1,700&display=swap" rel="stylesheet">
<style>
  :root{
    --red:#c0353e;
    --black:#0a0a0a;
    --white:#ffffff;
    --paper:#f7f7f7;
    --bg:#efefef;
    --band:#ebebeb;
    --line:#555;
    --field:#e2e4e7;
    --text:#1a1a1a;
  }
  *{box-sizing:border-box;margin:0;padding:0}
  html,body{width:1200px;height:782px;overflow:hidden;background:var(--bg)}
  body{position:relative;font-family:"Roboto",sans-serif;color:var(--text)}
  .page{position:absolute;top:82px;width:478px;height:618px;background:var(--paper);overflow:hidden}
  .page--physicians{left:104px}
  .page--form{left:628px}
  .abs{position:absolute}

  /* Physician side */
  .section-title{left:41px;top:51px;font-family:"Montserrat",sans-serif;font-size:14px;letter-spacing:3px;font-weight:400;padding-bottom:3px;border-bottom:2px solid var(--red)}
  .section-title b{font-weight:800}
  .brand{left:270px;top:46px;display:flex;align-items:center;gap:8px;font-family:"Montserrat",sans-serif;font-weight:800;font-size:21px;letter-spacing:2px;color:var(--red);line-height:1}
  .brand-dot{width:12px;height:12px;border-radius:50%;background:var(--red)}
  .physician-band{left:0;top:123px;width:478px;height:101px;background:var(--band)}
  .pill{position:absolute;height:23px;border-radius:12px;color:var(--white);font-family:"Montserrat",sans-serif;font-weight:600;font-size:10.5px;display:flex;align-items:center;justify-content:center;white-space:nowrap}
  .pill--black{background:var(--black)}
  .pill--red{background:var(--red)}
  .map{left:0;top:224px;width:478px;height:285px;background:linear-gradient(135deg,#eeeada 0%,#e6e6e6 35%,#e9e9e9 65%,#eef0e4 100%)}
  .footer{left:0;top:509px;width:478px;height:109px;background:var(--red);color:var(--white);text-align:center;font-family:"Montserrat",sans-serif}
  .footer-phone{position:absolute;top:23px;width:100%;font-size:10.5px}
  .footer-web{position:absolute;top:38px;width:100%;font-size:25px;font-weight:700;letter-spacing:-.3px}
  .footer-address{position:absolute;top:73px;width:100%;font-size:10.5px}

  /* Form side */
  .form-header{left:0;top:0;width:478px;height:121px;background:var(--red)}
  .title-light{left:24px;top:29px;font-family:"Montserrat",sans-serif;font-weight:400;font-size:29px;color:var(--white);letter-spacing:.2px;line-height:1}
  .title-bold{left:23px;top:58px;font-family:"Montserrat",sans-serif;font-weight:900;font-size:34.5px;color:var(--black);line-height:1;letter-spacing:-.4px}
  .schedule{left:297px;top:30px;width:160px;height:63px;background:var(--white);border-radius:6px;overflow:hidden}
  .schedule-head{background:var(--black);color:var(--white);font-family:"Montserrat",sans-serif;font-weight:800;font-size:13px;text-align:center;height:21px;line-height:22px;letter-spacing:.4px}
  .schedule-row{font-size:8px;padding:0 8px;height:20px;line-height:20px;font-weight:500}
  .schedule-row + .schedule-row{border-top:1px solid var(--red)}
  .bar{position:absolute;height:15px;color:var(--white);font-family:"Montserrat",sans-serif;font-weight:700;font-size:10px;letter-spacing:1.5px;display:flex;align-items:center;justify-content:center}
  .bar--red{background:var(--red)}
  .bar--black{background:var(--black)}
  .label{position:absolute;font-size:8px;white-space:nowrap}
  .rule{position:absolute;height:0;border-bottom:.7px solid var(--line)}
  .check{display:inline-block;width:8px;height:8px;border:.8px solid #333;vertical-align:-1px;margin-right:5px;background:var(--white)}
  .sexbox{display:inline-block;width:8px;height:8px;border:.7px solid #333;font-size:5.5px;line-height:7px;text-align:center;margin-left:4px;vertical-align:0}
  .inline-line{display:inline-block;border-bottom:.7px solid var(--line);vertical-align:-1px}
  .divider{left:21px;top:394px;width:436px;height:5px;background:#e4e4e4}
  .notice{left:21px;top:405px;width:440px;font-size:7.4px;font-style:italic;font-weight:700}
  .rules-list{position:absolute;list-style:none;width:180px;font-size:5.6px;line-height:1.35}
  .rules-list li{position:relative;padding-left:11px;margin-bottom:5px}
  .rules-list li svg{position:absolute;left:0;top:0;width:7px;height:7px}
  .ack{left:21px;top:507px;width:440px;font-size:6.4px;font-style:italic;font-weight:700;line-height:1.3}
  .sign{position:absolute;width:132px;height:31px;background:var(--field);border-radius:4px;overflow:hidden}
  .sign-head{height:13px;padding-left:9px;font-size:7.2px;line-height:13px;color:var(--white)}
  .sign--red .sign-head{background:var(--red)}
  .sign--black .sign-head{background:var(--black)}
  .referral{left:297px;top:532px;width:160px;height:66px;border-radius:4px;overflow:hidden;background:var(--field)}
  .referral-head{background:var(--black);color:var(--white);font-size:7.2px;height:18px;line-height:18px;padding-left:12px}
  .referral-row{font-size:6.5px;height:16px;line-height:16px;padding-left:15px;font-weight:500;border-bottom:1px solid var(--white)}
</style>
</head>
<body>

<section class="page page--physicians">
  <h2 class="abs section-title">OUR <b>PHYSICIAN</b></h2>
  <div class="abs brand"><span class="brand-dot"></span><span>CRESTFIELD<br>CARDIAC</span></div>

  <div class="abs physician-band">
    <span class="pill pill--black" style="left:24px;top:20px;width:134px">Dorian Velko, MD</span>
    <span class="pill pill--red" style="left:169px;top:20px;width:134px">L.N. Morvesti, MD</span>
    <span class="pill pill--black" style="left:315px;top:20px;width:133px">Ovila Brandt, MD</span>
    <span class="pill pill--black" style="left:-20px;top:57px;width:105px"></span>
    <span class="pill pill--red" style="left:99px;top:57px;width:134px">Tomas Velko, MD</span>
    <span class="pill pill--black" style="left:245px;top:57px;width:134px">Gerald Pompetti, MD</span>
    <span class="pill pill--black" style="left:392px;top:57px;width:110px"></span>
  </div>

  <div class="abs map" role="img" aria-label="Street map of the area around the clinic with a location pin marking the office"></div>

  <footer class="abs footer">
    <p class="footer-phone">Phone 832-417-2286 &nbsp;&nbsp;|&nbsp;&nbsp; Fax 832-417-2287</p>
    <p class="footer-web">www.crestfieldcardiac.example</p>
    <p class="footer-address">Crestfield Cardiac PLLC, 712 Harrow Ln. Ste. K, Melrick, TX 77431</p>
  </footer>
</section>

<section class="page page--form">
  <header class="abs form-header">
    <h1 class="abs title-light">CALCIUM SCORE</h1>
    <p class="abs title-bold">HEART SCAN</p>
    <div class="abs schedule">
      <div class="schedule-head">TEST SCHEDULE</div>
      <div class="schedule-row">TEST DATE:</div>
      <div class="schedule-row">TEST TIME:</div>
    </div>
  </header>

  <div class="bar bar--red" style="left:21px;top:138px;width:225px;clip-path:polygon(0 0,100% 0,97% 100%,0 100%)">PATIENT INFORMATION</div>
  <div class="bar bar--black" style="left:240px;top:138px;width:217px;clip-path:polygon(3% 0,100% 0,100% 100%,0 100%)">CONTACT INFORMATION</div>

  <span class="label" style="left:21px;top:167px">Last Name</span>
  <span class="label" style="left:100px;top:167px">First Name</span>
  <span class="label" style="left:177px;top:167px">MI</span>
  <span class="label" style="left:250px;top:167px">Address</span>
  <span class="rule" style="left:286px;top:174px;width:171px"></span>
  <span class="rule" style="left:21px;top:192px;width:72px"></span>
  <span class="rule" style="left:100px;top:192px;width:72px"></span>
  <span class="rule" style="left:177px;top:192px;width:53px"></span>
  <span class="rule" style="left:250px;top:192px;width:207px"></span>

  <span class="label" style="left:21px;top:207px">Date of Birth</span>
  <span class="label" style="left:129px;top:207px">Account No.</span>
  <span class="label" style="left:250px;top:207px">Home Phone No.</span>
  <span class="label" style="left:357px;top:207px">Mobile Phone No.</span>
  <span class="rule" style="left:21px;top:230px;width:101px"></span>
  <span class="rule" style="left:129px;top:230px;width:101px"></span>
  <span class="rule" style="left:250px;top:230px;width:101px"></span>
  <span class="rule" style="left:357px;top:230px;width:100px"></span>

  <div class="bar bar--black" style="left:21px;top:246px;width:436px;font-size:11px">MEDICAL INFORMATION</div>

  <span class="label" style="left:21px;top:275px">Sex: <span class="sexbox">F</span><span class="sexbox">M</span></span>
  <span class="label" style="left:79px;top:275px">Height: <span class="inline-line" style="width:76px"></span></span>
  <span class="label" style="left:197px;top:275px">Weight <span class="inline-line" style="width:76px"></span></span>
  <span class="label" style="left:316px;top:275px">Race: <span class="inline-line" style="width:117px"></span></span>

  <span class="label" style="left:21px;top:296px">Diagnosis:</span>
  <span class="rule" style="left:66px;top:304px;width:391px"></span>

  <span class="label" style="left:21px;top:319px"><i class="check"></i>PCI (no. of stents: <span class="inline-line" style="width:52px"></span> )</span>
  <span class="label" style="left:180px;top:319px"><i class="check"></i>CABG (no. of vessels: <span class="inline-line" style="width:45px"></span> )</span>
  <span class="label" style="left:341px;top:319px"><i class="check"></i>MI (last event: <span class="inline-line" style="width:48px"></span>)</span>

  <span class="label" style="left:21px;top:345px"><i class="check"></i>PCM/ICD</span>
  <span class="label" style="left:97px;top:345px"><i class="check"></i>Diabetes</span>
  <span class="label" style="left:171px;top:345px"><i class="check"></i>Claustrophobia</span>
  <span class="label" style="left:268px;top:345px"><i class="check"></i>Asthma</span>
  <span class="label" style="left:337px;top:345px"><i class="check"></i>Emphysema</span>
  <span class="label" style="left:422px;top:345px"><i class="check"></i>COPD</span>

  <span class="label" style="left:21px;top:369px">LMP: <span class="inline-line" style="width:104px"></span></span>
  <span class="label" style="left:152px;top:369px"><i class="check"></i>BHCG</span>
  <span class="label" style="left:205px;top:369px"><i class="check"></i>Tubal ligation</span>
  <span class="label" style="left:282px;top:369px"><i class="check"></i>Post-menopause&gt;1 year</span>
  <span class="label" style="left:398px;top:369px"><i class="check"></i>Hysterectomy</span>

  <div class="abs divider"></div>
  <p class="abs notice">Please read the following instructions carefully. You might be rescheduled if any of the following instructions are not met.</p>

  <ul class="rules-list" style="left:43px;top:424px">
    <li><svg viewBox="0 0 10 10"><circle cx="5" cy="5" r="5" fill="#c0353e"/><path d="M2.6 5.2l1.7 1.7 3.2-3.4" stroke="#fff" stroke-width="1.3" fill="none"/></svg>AVOID caffeine containing products (coffee, tea, soda, chocolate, energy drinks, or some over the counter medications) for 4 hours prior to testing.</li>
    <li><svg viewBox="0 0 10 10"><circle cx="5" cy="5" r="5" fill="#c0353e"/><path d="M2.6 5.2l1.7 1.7 3.2-3.4" stroke="#fff" stroke-width="1.3" fill="none"/></svg>AVOID smoking for 4 hours prior to testing.</li>
    <li><svg viewBox="0 0 10 10"><circle cx="5" cy="5" r="5" fill="#c0353e"/><path d="M2.6 5.2l1.7 1.7 3.2-3.4" stroke="#fff" stroke-width="1.3" fill="none"/></svg>AVOID eating or drinking anything except water for 4 hours prior to testing.</li>
    <li><svg viewBox="0 0 10 10"><circle cx="5" cy="5" r="5" fill="#c0353e"/><path d="M2.6 5.2l1.7 1.7 3.2-3.4" stroke="#fff" stroke-width="1.3" fill="none"/></svg>Arrive 15 minutes early for your appointment time.</li>
  </ul>
  <ul class="rules-list" style="left:261px;top:424px">
    <li><svg viewBox="0 0 10 10"><circle cx="5" cy="5" r="5" fill="#c0353e"/><path d="M2.6 5.2l1.7 1.7 3.2-3.4" stroke="#fff" stroke-width="1.3" fill="none"/></svg>Wear comfortable clothing. Remove any metal objects, such as jewelry or piercings. Women will be asked to remove bras containing metal underwire.</li>
    <li><svg viewBox="0 0 10 10"><circle cx="5" cy="5" r="5" fill="#c0353e"/><path d="M2.6 5.2l1.7 1.7 3.2-3.4" stroke="#fff" stroke-width="1.3" fill="none"/></svg>Inform your physician or the staff if you are claustrophobic or have a problem staying in restricted environments for any length of time.</li>
    <li><svg viewBox="0 0 10 10"><circle cx="5" cy="5" r="5" fill="#c0353e"/><path d="M2.6 5.2l1.7 1.7 3.2-3.4" stroke="#fff" stroke-width="1.3" fill="none"/></svg>Inform the physician or the staff if you are or think you might be pregnant.</li>
  </ul>

  <p class="abs ack">I hereby acknowledge that the instructions and procedures pertinent to this study were explained thoroughly, I had time to ask questions, and these questions were addressed satisfactorily.</p>

  <div class="sign sign--red" style="left:21px;top:532px"><div class="sign-head">Patient's Print Name</div></div>
  <div class="sign sign--red" style="left:159px;top:532px"><div class="sign-head">Patient's Signature</div></div>
  <div class="sign sign--black" style="left:21px;top:567px"><div class="sign-head">Prescriber's Print Name</div></div>
  <div class="sign sign--black" style="left:159px;top:567px"><div class="sign-head">Prescriber's Signature</div></div>

  <div class="abs referral">
    <div class="referral-head">Referring Physician Contact Information</div>
    <div class="referral-row">ORDER DATE:</div>
    <div class="referral-row">TEL NO.:</div>
    <div class="referral-row">FAX NO.:</div>
  </div>
</section>

</body>
</html>
```